Workvine banner ad for roofing company

We need an ad created for a Workvine banner advertising campaign for a UK based roofing company.

The design should have a large photograph on the background (see attached).
The design should have our Ratewell rating (5 stars).
There should be a large text header at the top which reads "Your local roofing experts"

The following services should be listed:
- New roofs
- General roof repairs
- Drone surveys
- Single ply roofing
- Steel cladding
- Asbestos removal

The company logo needs to be visible (attached). Also the company telephone number 020 7946 0321 and website www.brantleyroofing.com

The advert needs to be horizontal/landscape design. For full spec, please see here: https://business.workvine-example.com/marketing-solutions/success/ads-guide/single-image-ads

Size required: 1.91:1 - 1200 x 628 pixels

```html
<!DOCTYPE html>
<html lang="en">
<head>
<meta charset="utf-8">
<title>Brantley Roofing – Banner</title>
<link rel="stylesheet" href="https://fonts.googleapis.com/css2?family=Montserrat:wght@400;500;600;700;800&display=swap">
<style>
  :root{
    --navy:#0f4678;
    --ink:#0b2d52;
    --cyan:#00a9dc;
    --star:#00a9dc;
    --white:#ffffff;
    --paper:#f4f5f6;
    --stage:#c0c0c0;
    --text:#1c2a36;
  }
  *{box-sizing:border-box;margin:0;padding:0}
  html,body{width:1200px;height:680px;overflow:hidden;background:var(--stage)}
  .banner{
    position:absolute;left:0;top:26px;width:1200px;height:628px;overflow:hidden;
    background:linear-gradient(120deg,#ffffff 0%,var(--paper) 45%,#e6e7e9 100%);
    font-family:"Montserrat",sans-serif;color:var(--navy);
  }
  .shapes{position:absolute;inset:0}
  .logo-tab{
    position:absolute;left:58px;top:0;width:196px;height:148px;background:var(--navy);
    border-radius:0 0 98px 98px / 0 0 70px 70px;
    display:flex;align-items:center;justify-content:center;gap:8px;
  }
  .logo-tab .mark{width:12px;height:12px;border-radius:50%;background:var(--white)}
  .logo-tab .name{color:var(--white);font-weight:700;font-size:20px;letter-spacing:-0.5px}
  .headline{
    position:absolute;left:60px;top:168px;font-weight:800;font-size:46px;line-height:49px;
    text-transform:uppercase;letter-spacing:-0.3px;
  }
  .services-band{
    position:absolute;left:0;top:296px;width:254px;height:40px;background:var(--cyan);
    border-radius:0 20px 20px 0;padding-left:63px;
    font-weight:700;font-size:20px;line-height:40px;color:var(--ink);
  }
  .service-list{position:absolute;top:366px;list-style:none}
  .service-list li{
    display:flex;align-items:center;gap:8px;height:26px;
    font-size:15px;font-weight:500;letter-spacing:0.8px;color:var(--text);
  }
  .service-list.col-a{left:63px}
  .service-list.col-b{left:234px}
  .tick{width:21px;height:21px;flex:none}
  .more-info{
    position:absolute;left:63px;top:469px;width:183px;height:39px;border-radius:20px;
    background:var(--navy);color:var(--white);font-weight:700;font-size:21px;
    text-align:center;line-height:39px;letter-spacing:0.3px;
  }
  .rating{
    position:absolute;left:266px;top:469px;height:39px;
    display:flex;flex-direction:column;justify-content:center;gap:2px;
  }
  .rating .source{font-size:13px;font-weight:600;color:var(--ink);letter-spacing:0.3px}
  .rating .stars{display:flex;gap:3px}
  .rating .star{width:17px;height:17px;fill:var(--star)}
  .contact{position:absolute;left:64px;top:543px;display:flex;align-items:center;gap:10px;color:var(--white)}
  .contact .phone-icon{width:52px;height:52px;flex:none}
  .contact .label{font-size:14px;font-weight:500;line-height:17px}
  .contact .number{font-size:20px;font-weight:700;letter-spacing:2px;line-height:24px}
  .contact .website{font-size:13px;font-weight:500;letter-spacing:0.4px;line-height:18px}
</style>
</head>
<body>
<div class="banner">
  <svg class="shapes" width="1200" height="628" viewBox="0 0 1200 628">
    <defs>
      <linearGradient id="aerial" x1="0" y1="0" x2="1" y2="1">
        <stop offset="0" stop-color="#6f8a5a"/><stop offset="0.5" stop-color="#b9a58d"/><stop offset="1" stop-color="#5d7a4c"/>
      </linearGradient>
      <linearGradient id="roofA" x1="0" y1="0" x2="1" y2="1">
        <stop offset="0" stop-color="#c9d6e2"/><stop offset="1" stop-color="#5d6670"/>
      </linearGradient>
      <linearGradient id="roofB" x1="0" y1="0" x2="1" y2="1">
        <stop offset="0" stop-color="#8a8f92"/><stop offset="1" stop-color="#3f4a56"/>
      </linearGradient>
      <linearGradient id="roofC" x1="0" y1="0" x2="0" y2="1">
        <stop offset="0" stop-color="#9a9a9a"/><stop offset="1" stop-color="#2b2b2b"/>
      </linearGradient>
    </defs>
    <path class="panel-right" d="M822 0H1200V628H822Q640 500 665 310Q690 110 822 0Z" fill="var(--navy)"/>
    <ellipse role="img" aria-label="Aerial photograph of a campus of buildings with grey roofs and green grounds" cx="945" cy="313" rx="245" ry="252" fill="url(#aerial)"/>
    <g stroke="var(--cyan)" stroke-width="6">
      <circle role="img" aria-label="Photograph of a standing-seam metal roof" cx="747" cy="117" r="95" fill="url(#roofA)"/>
      <circle role="img" aria-label="Photograph of a long industrial roof with rooflights" cx="632" cy="314" r="95" fill="url(#roofB)"/>
      <circle role="img" aria-label="Black and white photograph of roof plant on a flat roof" cx="747" cy="511" r="95" fill="url(#roofC)"/>
    </g>
    <circle cx="440" cy="57" r="19" fill="var(--cyan)"/>
    <circle cx="476" cy="79" r="29" fill="var(--navy)" stroke="var(--cyan)" stroke-width="4"/>
    <circle cx="516" cy="558" r="28" fill="var(--cyan)"/>
    <circle cx="544" cy="577" r="17" fill="var(--navy)"/>
    <path class="contact-panel" d="M0 524H235Q335 524 382 628H0Z" fill="var(--navy)"/>
  </svg>

  <div class="logo-tab"><span class="mark"></span><span class="name">brantleyroofing</span></div>

  <h1 class="headline">Your local<br>roofing experts</h1>

  <div class="services-band">OUR SERVICES</div>

  <ul class="service-list col-a">
    <li><svg class="tick" viewBox="0 0 22 22"><circle cx="11" cy="11" r="9.5" fill="none" stroke="#1c2a36" stroke-width="1.6"/><path d="M6.5 11.2l3 3 6-6.4" fill="none" stroke="#1c2a36" stroke-width="1.8" stroke-linecap="round" stroke-linejoin="round"/></svg>New Roofs</li>
    <li><svg class="tick" viewBox="0 0 22 22"><circle cx="11" cy="11" r="9.5" fill="none" stroke="#1c2a36" stroke-width="1.6"/><path d="M6.5 11.2l3 3 6-6.4" fill="none" stroke="#1c2a36" stroke-width="1.8" stroke-linecap="round" stroke-linejoin="round"/></svg>Drone Surveys</li>
    <li><svg class="tick" viewBox="0 0 22 22"><circle cx="11" cy="11" r="9.5" fill="none" stroke="#1c2a36" stroke-width="1.6"/><path d="M6.5 11.2l3 3 6-6.4" fill="none" stroke="#1c2a36" stroke-width="1.8" stroke-linecap="round" stroke-linejoin="round"/></svg>Steel Cladding</li>
  </ul>
  <ul class="service-list col-b">
    <li><svg class="tick" viewBox="0 0 22 22"><circle cx="11" cy="11" r="9.5" fill="none" stroke="#1c2a36" stroke-width="1.6"/><path d="M6.5 11.2l3 3 6-6.4" fill="none" stroke="#1c2a36" stroke-width="1.8" stroke-linecap="round" stroke-linejoin="round"/></svg>General Roof Repairs</li>
    <li><svg class="tick" viewBox="0 0 22 22"><circle cx="11" cy="11" r="9.5" fill="none" stroke="#1c2a36" stroke-width="1.6"/><path d="M6.5 11.2l3 3 6-6.4" fill="none" stroke="#1c2a36" stroke-width="1.8" stroke-linecap="round" stroke-linejoin="round"/></svg>Single Ply Roofing</li>
    <li><svg class="tick" viewBox="0 0 22 22"><circle cx="11" cy="11" r="9.5" fill="none" stroke="#1c2a36" stroke-width="1.6"/><path d="M6.5 11.2l3 3 6-6.4" fill="none" stroke="#1c2a36" stroke-width="1.8" stroke-linecap="round" stroke-linejoin="round"/></svg>Asbestos Removal</li>
  </ul>

  <div class="more-info">MORE INFO</div>

  <div class="rating" aria-label="Rated 5 out of 5 on Ratewell">
    <span class="source">Rated 5/5 on Ratewell</span>
    <span class="stars">
      <svg class="star" viewBox="0 0 20 20"><path d="M10 1.5l2.6 5.4 5.9.8-4.3 4.1 1 5.8L10 14.8l-5.2 2.8 1-5.8L1.5 7.7l5.9-.8z"/></svg>
      <svg class="star" viewBox="0 0 20 20"><path d="M10 1.5l2.6 5.4 5.9.8-4.3 4.1 1 5.8L10 14.8l-5.2 2.8 1-5.8L1.5 7.7l5.9-.8z"/></svg>
      <svg class="star" viewBox="0 0 20 20"><path d="M10 1.5l2.6 5.4 5.9.8-4.3 4.1 1 5.8L10 14.8l-5.2 2.8 1-5.8L1.5 7.7l5.9-.8z"/></svg>
      <svg class="star" viewBox="0 0 20 20"><path d="M10 1.5l2.6 5.4 5.9.8-4.3 4.1 1 5.8L10 14.8l-5.2 2.8 1-5.8L1.5 7.7l5.9-.8z"/></svg>
      <svg class="star" viewBox="0 0 20 20"><path d="M10 1.5l2.6 5.4 5.9.8-4.3 4.1 1 5.8L10 14.8l-5.2 2.8 1-5.8L1.5 7.7l5.9-.8z"/></svg>
    </span>
  </div>

  <div class="contact">
    <svg class="phone-icon" viewBox="0 0 52 52">
      <circle cx="26" cy="26" r="25" fill="var(--cyan)"/>
      <circle cx="26" cy="26" r="20" fill="none" stroke="var(--white)" stroke-width="2.5"/>
      <path d="M19.5 16.5c1-.9 2.3-.8 3 .3l1.8 2.9c.5.9.3 2-.5 2.6l-1.3 1c.9 2.3 2.7 4.2 5 5.2l1-1.3c.6-.8 1.7-1 2.6-.5l2.9 1.8c1.1.7 1.2 2 .3 3l-1.4 1.4c-1.2 1.2-3 1.5-4.6.8-5-2.2-8.8-6-11-11-.7-1.6-.4-3.4.8-4.6z" fill="var(--white)"/>
    </svg>
    <div>
      <div class="label">Contact Us</div>
      <div class="number">020 7946 0321</div>
      <div class="website">www.brantleyroofing.com</div>
    </div>
  </div>
</div>
</body>
</html>
```